Maple Hollow Canine Massage Needs a Business Card Design

Maple Hollow Canine Massage is a new therapeutic canine massage company located in Nederland, Colorado. I need a business card design that include my logo and basic contact information.

Target Market(s)

Pet owners, veterinarians

Industry/Entity Type

Business

Contact Information for Business Card

Lydia Ferrow, CCMT
303.518.7269
lydia@maplehollowmassage.example
www.maplehollowmassage.example

Colors
6c459b
886aae
b8a6cd
a64599
b768aa
d3a5cc
fbed22

Requirements
Must have
• Font should be similar to font in logo.

```html
<!DOCTYPE html>
<html lang="en">
<head>
<meta charset="utf-8">
<title>Maple Hollow Canine Massage – Business Card</title>
<link rel="stylesheet" href="https://fonts.googleapis.com/css2?family=Open+Sans:wght@400;600;700&display=swap">
<style>
  :root {
    --stage: #e9e6e1;
    --card-black: #0b0b0b;
    --card-sheen: #232323;
    --band-white: #f2f2f2;
    --purple: #6c459b;
    --purple-soft: #886aae;
    --yellow: #fbed22;
    --text-white: #ffffff;
    --divider: #555555;
  }
  html, body {
    margin: 0;
    width: 1200px;
    height: 1022px;
    overflow: hidden;
    background: var(--stage);
    font-family: "Open Sans", Arial, sans-serif;
  }
  .card {
    position: absolute;
    left: 75px;
    top: 211px;
    width: 1050px;
    height: 600px;
    border-radius: 28px;
    overflow: hidden;
    background: linear-gradient(160deg, var(--card-sheen) 0%, var(--card-black) 45%, var(--card-black) 100%);
    box-shadow: 0 18px 40px rgba(0,0,0,0.25);
  }
  .brand {
    position: absolute;
    left: 90px;
    top: 70px;
    width: 320px;
    text-align: center;
  }
  .brand-disc {
    display: block;
    width: 230px;
    height: 230px;
    margin: 0 auto 24px;
    border-radius: 50%;
    background: var(--purple);
  }
  .brand-name {
    margin: 0;
    color: var(--text-white);
    font-weight: 600;
    font-size: 26px;
    line-height: 1.3;
    letter-spacing: 0.5px;
  }
  .identity {
    position: absolute;
    left: 520px;
    top: 95px;
  }
  .person-name {
    margin: 0;
    color: var(--text-white);
    font-weight: 700;
    font-size: 54px;
    line-height: 1.1;
  }
  .person-title {
    margin: 4px 0 0;
    color: var(--yellow);
    font-size: 26px;
    font-weight: 400;
  }
  .divider {
    width: 180px;
    height: 2px;
    margin: 26px 0 26px -60px;
    background: linear-gradient(90deg, transparent, var(--divider), transparent);
  }
  .contact-list {
    list-style: none;
    margin: 0;
    padding: 0;
  }
  .contact-item {
    display: flex;
    align-items: center;
    gap: 16px;
    color: var(--text-white);
    font-size: 24px;
    line-height: 1.7;
  }
  .contact-icon {
    width: 18px;
    height: 18px;
    flex: none;
  }
  .web-band {
    position: absolute;
    left: 0;
    right: 0;
    bottom: 0;
    height: 86px;
    background: var(--band-white);
    display: flex;
    align-items: center;
    justify-content: flex-end;
    padding-right: 60px;
    color: var(--purple-soft);
    font-size: 28px;
    letter-spacing: 0.5px;
  }
</style>
</head>
<body>
  <section class="card" aria-label="Business card front">
    <div class="brand">
      <span class="brand-disc"></span>
      <p class="brand-name">Maple Hollow<br>Canine Massage</p>
    </div>

    <div class="identity">
      <h1 class="person-name">Lydia Ferrow</h1>
      <p class="person-title">CCMT</p>
      <div class="divider"></div>
      <ul class="contact-list">
        <li class="contact-item">
          <svg class="contact-icon" viewBox="0 0 18 18"><rect x="4" y="1.5" width="10" height="15" rx="2" fill="none" stroke="#fbed22" stroke-width="2"/><rect x="7" y="13" width="4" height="1.5" fill="#fbed22"/></svg>
          303.518.7269
        </li>
        <li class="contact-item">
          <svg class="contact-icon" viewBox="0 0 18 18"><rect x="1.5" y="3" width="15" height="12" fill="none" stroke="#fbed22" stroke-width="2"/><path d="M2 4 L9 10 L16 4" fill="none" stroke="#fbed22" stroke-width="2"/></svg>
          lydia@maplehollowmassage.example
        </li>
        <li class="contact-item">
          <svg class="contact-icon" viewBox="0 0 18 18"><circle cx="9" cy="9" r="7.5" fill="none" stroke="#fbed22" stroke-width="1.8"/><ellipse cx="9" cy="9" rx="3.2" ry="7.5" fill="none" stroke="#fbed22" stroke-width="1.5"/><line x1="1.5" y1="9" x2="16.5" y2="9" stroke="#fbed22" stroke-width="1.5"/></svg>
          www.maplehollowmassage.example
        </li>
      </ul>
    </div>

    <div class="web-band">www.maplehollowmassage.example</div>
  </section>
</body>
</html>
```